Credit card acceptance poster

I need a poster explaining to my customers that the washers and dryers at my laundromat accept credit card payments and most mobile wallet payments. I have attached a flyer I made. It looks terrible so I need help. The cc readers accept: NORO, BRUNOVAULT, TALVEXIA, HOLBORNE TRAMLEY, ZORBIT PAY, WENDLE PAY, AND KIRUVEX PAY.

Colors
0054AA
0677BA
7BADD7
CADEEF
E8F1F8

```html
<!DOCTYPE html>
<html lang="en">
<head>
<meta charset="utf-8">
<title>Sudsmore Laundromat – Card Payments Poster</title>
<link rel="stylesheet" href="https://fonts.googleapis.com/css2?family=Bebas+Neue&family=Poppins:ital,wght@0,600;0,700;1,300;1,600&display=swap">
<style>
  :root {
    --blue-deep: #0054AA;
    --blue-mid: #0677BA;
    --blue-soft: #7BADD7;
    --blue-pale: #CADEEF;
    --blue-mist: #E8F1F8;
    --ink: #0b0b0b;
    --navy: #0d1f4a;
    --page: #ffffff;
  }
  * { box-sizing: border-box; margin: 0; padding: 0; }
  html, body { width: 764px; height: 1200px; overflow: hidden; background: var(--page); }
  .poster {
    position: absolute; left: 0; top: 106px;
    width: 764px; height: 988px;
    background: linear-gradient(160deg, #ffffff 0%, #f6f9fc 55%, #ffffff 100%);
    box-shadow: 0 6px 24px rgba(0,0,0,0.18);
    overflow: hidden;
    font-family: "Poppins", sans-serif;
  }
  .hero-photo {
    position: absolute; left: 0; top: 0; width: 764px; height: 361px;
    background: linear-gradient(100deg, #c9d3da 0%, #e6ebee 35%, #d3dde3 60%, #b8c6cc 100%);
  }
  .band {
    position: absolute; left: 0; width: 764px;
    background: linear-gradient(90deg, var(--blue-soft) 0%, var(--blue-mid) 70%, var(--blue-deep) 100%);
  }
  .band--top { top: 361px; height: 32px; }
  .band--bottom { top: 970px; height: 18px; }
  .headline {
    position: absolute; left: 84px; top: 404px;
    font-family: "Bebas Neue", sans-serif; line-height: 1;
  }
  .headline__question { display: block; font-size: 96px; color: var(--blue-mid); letter-spacing: -0.5px; }
  .headline__answer { display: block; font-size: 140px; color: var(--ink); letter-spacing: -1px; margin-top: -6px; }
  .intro {
    position: absolute; left: 84px; top: 662px; width: 292px;
    font-size: 26px; font-style: italic; font-weight: 300; line-height: 35px; color: var(--ink);
    white-space: nowrap;
  }
  .reader-art {
    position: absolute; left: 386px; top: 620px; width: 344px; height: 216px;
    background: linear-gradient(135deg, #9aa3ab 0%, #3f5fa8 45%, #1b2f6a 70%, #c5ccd2 100%);
    border-radius: 10px;
  }
  .tagline {
    position: absolute; left: 430px; top: 846px; width: 334px; height: 40px;
    background: linear-gradient(90deg, rgba(232,241,248,0) 0%, var(--blue-pale) 30%, var(--blue-soft) 70%, var(--blue-mid) 100%);
    font-size: 18px; font-weight: 600; font-style: italic; color: var(--navy);
    display: flex; align-items: center; justify-content: flex-end; padding-right: 24px;
  }
  .brand {
    position: absolute; left: 46px; top: 850px;
    display: flex; align-items: center; gap: 10px;
    font-weight: 700; color: var(--blue-mid); line-height: 1.05;
  }
  .brand__dot { width: 38px; height: 38px; border-radius: 50%; background: var(--blue-mid); flex: none; }
  .brand__name { font-size: 30px; }
  .brand__kind { display: block; font-size: 17px; letter-spacing: 2px; }
  .payments {
    position: absolute; left: 352px; top: 916px; width: 390px;
    display: flex; flex-wrap: nowrap; gap: 3px; justify-content: flex-end;
    list-style: none;
  }
  .payments__item {
    font-size: 6.5px; font-weight: 600; color: var(--navy);
    background: #fff; border: 1px solid var(--blue-pale); border-radius: 6px;
    padding: 3px 4px; white-space: nowrap;
  }
</style>
</head>
<body>
  <main class="poster">
    <div class="hero-photo" role="img" aria-label="Photo of a hand tapping a smartphone showing a payment confirmation at a laundromat washer's card reader"></div>
    <div class="band band--top"></div>

    <h1 class="headline">
      <span class="headline__question">No bills or coins?</span>
      <span class="headline__answer">No problem!</span>
    </h1>

    <p class="intro">Our machines<br>accept Credit Card<br>Payments and most<br>Mobile Wallet Apps</p>

    <div class="reader-art" role="img" aria-label="Illustration of a machine card reader with a smartphone and a credit card"></div>

    <div class="tagline">Pay With Ease, Every Time!</div>

    <div class="brand">
      <span class="brand__dot"></span>
      <span class="brand__name">SUDSMORE<span class="brand__kind">LAUNDROMAT</span></span>
    </div>

    <ul class="payments">
      <li class="payments__item">BRUNOVAULT</li>
      <li class="payments__item">HOLBORNE TRAMLEY</li>
      <li class="payments__item">KIRUVEX PAY</li>
      <li class="payments__item">WENDLE PAY</li>
      <li class="payments__item">NORO</li>
      <li class="payments__item">TALVEXIA</li>
      <li class="payments__item">ZORBIT PAY</li>
    </ul>

    <div class="band band--bottom"></div>
  </main>
</body>
</html>
```